New local Orchid nursery branding

We need a business card designed for our small local company in Darwin, Australia that grows orchids, called Blooms at Carrow.
We will be running private sales from our property, and handing these out at local events for perspective customers.

We would like to see designs that are simple, and able to be used with minimal colours and containing an orchid, preferably a stylised representation instead of a photo.
The eventual hope is to take this into larger formats to create our company logo/branding etc, but for now we just need business cards.

Target Market(s)

Local Orchid

Industry/Entity Type

Business

Contact Information for Business Card

Company Name
Logo
Name
Phone Number
Street Address
Email Address (less prominent than rest of the text)

Font styles to use
Sans Serif

Requirements
Must have
• Name of the company, which is Blooms at Carrow
Nice to have
• stylised orchid logo
Should not have
• too many colours

```html
<!DOCTYPE html>
<html lang="en">
<head>
<meta charset="utf-8">
<title>Blooms at Carrow — Business Card</title>
<link rel="stylesheet" href="https://fonts.googleapis.com/css2?family=Montserrat:wght@600;700&family=Open+Sans:wght@400;600&display=swap">
<style>
  :root {
    --navy: #10203f;
    --navy-light: #3a4f6e;
    --magenta: #b2357c;
    --purple: #7b4aa8;
    --ink: #263550;
    --card: #ffffff;
    --backdrop: #e9e6e1;
  }
  * { margin: 0; padding: 0; box-sizing: border-box; }
  html, body {
    width: 1200px; height: 1023px; overflow: hidden;
    background: var(--backdrop);
  }
  .business-card {
    position: absolute; left: 150px; top: 254px;
    width: 900px; height: 514px;
    background: var(--card);
    border-radius: 28px;
    overflow: hidden;
    box-shadow: 0 10px 30px rgba(0,0,0,0.18);
  }
  .edge-band { position: absolute; inset: 0; width: 100%; height: 100%; }
  .brand {
    position: absolute; left: 60px; top: 190px;
    display: flex; align-items: center; gap: 18px;
  }
  .brand-dot {
    width: 64px; height: 64px; border-radius: 50%;
    background: var(--purple);
    flex: none;
  }
  .brand-name {
    font-family: "Montserrat", sans-serif;
    font-weight: 700; font-size: 30px; line-height: 1.1;
    letter-spacing: 1px; text-transform: uppercase;
    color: var(--ink);
  }
  .contact {
    position: absolute; left: 385px; top: 118px;
    font-family: "Open Sans", sans-serif;
    color: var(--magenta);
  }
  .contact-name {
    font-family: "Montserrat", sans-serif;
    font-weight: 700; font-size: 24px; color: var(--ink);
    text-transform: uppercase;
  }
  .contact-role { font-size: 18px; margin-top: 2px; }
  .contact-lines { list-style: none; margin-top: 30px; font-size: 18px; line-height: 1.6; }
  .contact-lines li { display: flex; align-items: center; gap: 10px; white-space: nowrap; }
  .contact-lines .email { font-size: 15px; }
  .contact-lines svg { width: 16px; height: 16px; fill: var(--ink); flex: none; }
  .contact-address { margin-top: 26px; font-size: 18px; line-height: 1.5; }
</style>
</head>
<body>
  <main class="business-card">
    <svg class="edge-band" viewBox="0 0 900 514" preserveAspectRatio="none" aria-hidden="true">
      <path d="M735 0 Q755 300 645 514 L900 514 L900 0 Z" fill="var(--navy)"/>
      <path d="M675 0 Q725 300 595 514 L620 514 Q740 300 697 0 Z" fill="var(--magenta)"/>
      <path d="M697 0 Q740 300 620 514 L645 514 Q755 300 735 0 Z" fill="var(--card)"/>
      <path d="M810 514 Q880 420 900 330 L900 514 Z" fill="var(--navy-light)" opacity="0.5"/>
    </svg>

    <div class="brand">
      <span class="brand-dot"></span>
      <span class="brand-name">Blooms<br>at Carrow</span>
    </div>

    <section class="contact">
      <h1 class="contact-name">Dana Whitlow</h1>
      <p class="contact-role">Director</p>
      <ul class="contact-lines">
        <li>
          <svg viewBox="0 0 24 24"><path d="M6.6 10.8a15.1 15.1 0 0 0 6.6 6.6l2.2-2.2a1 1 0 0 1 1-.25 11.4 11.4 0 0 0 3.6.57 1 1 0 0 1 1 1V20a1 1 0 0 1-1 1A17 17 0 0 1 3 4a1 1 0 0 1 1-1h3.5a1 1 0 0 1 1 1c0 1.25.2 2.45.57 3.57a1 1 0 0 1-.25 1z"/></svg>
          0491 570 156
        </li>
        <li class="email">
          <svg viewBox="0 0 24 24"><path d="M2 5h20v14H2z M2 5l10 8 10-8" fill="none" stroke="var(--ink)" stroke-width="2"/></svg>
          dwhitlow@bloomsatcarrow.com.au
        </li>
      </ul>
      <p class="contact-address">BCom, 27 Marlin Court<br>Rapid Creek, NT 0810</p>
    </section>
  </main>
</body>
</html>
```